Label Design for 2x Chutney Products

We need a label design for 2x Chutney Products.
Zintara Chutney - Red Chili
Zintara Chutney - Green Chili & Coriander
See attached pictures. This is just sample pictures so you get an impression of the product and the colors. Both labels to have as title the generic name "Zintara Chutney" and then added either Red Chili or Green Chili & Coriander. The different terms needs to be good readable and can differ in font/color/size, or in the same style if this makes more sense from design point (as I am not a designer). The labels later on need to be editable in the way that the ingredient list, nutrition list, basis company and production information can be added. If this needs to be done directly and cannot be edited later on please let know. Editable design related the additional text also would be good as the additional information need to be added in different languages (Dutch. German and perhaps French). No clue how this is to be implemented but looking forward to receive some input/solutions on this.
I already had a project to create the company logo. I consider this logo to be used as the product logo and not the company logo. A different company logo later on can be designed from new. This logo is here attached. Either to work with this logo and use it as product logo (perhaps revise the colors) and add the product description or create a new logo for the product from scratch if you feel too. The logo itself should be easily readable for the product name/description and the colors appealing to such product and of course customers.
Please contact if any clarification needed. Thanks in advance for your efforts and ideas for this project.

Industry/Entity Type

Food

Other font styles liked:
• Asian Touch

Requirements
Nice to have
• If possible "simply" editable for text fields in order to add/revise the ingredient list, nutrition list, revise to different languages.

```html
<!DOCTYPE html>
<html lang="en">
<head>
<meta charset="utf-8">
<title>Zintara Chutney – Label Set</title>
<link rel="stylesheet" href="https://fonts.googleapis.com/css2?family=Bebas+Neue&display=swap">
<style>
  :root {
    --page: #ffffff;
    --label-cream: #e2dfca;
    --ink: #232323;
    --chili-red: #d6363b;
    --chili-red-dark: #b10f12;
    --leaf-green: #7cbd3f;
    --leaf-green-dark: #5a9818;
    --rule-red: #cf2f2f;
    --rule-green: #7dbb3a;
    --tag-black: #1c1c1c;
    --tag-text: #f4f4f4;
  }
  * { margin: 0; padding: 0; box-sizing: border-box; }
  html, body {
    width: 1200px; height: 818px; overflow: hidden;
    background: var(--page);
    font-family: "Bebas Neue", "Oswald", sans-serif;
  }
  .canvas { position: relative; width: 1200px; height: 818px; }

  .label {
    position: absolute; top: 188px;
    width: 536px; height: 443px;
    background: var(--label-cream);
    overflow: hidden;
  }
  .label--red { left: 40px; }
  .label--green { left: 624px; }

  .brand { position: absolute; left: 34px; top: 38px; display: flex; align-items: center; }
  .brand__dot {
    width: 66px; height: 66px; border-radius: 50%;
    background: var(--chili-red);
    margin-right: 12px;
  }
  .brand__name {
    font-size: 60px; line-height: 1; letter-spacing: 3px;
    color: var(--ink); white-space: nowrap;
  }
  .rule { position: absolute; top: 111px; height: 3px; }
  .rule--red { left: 178px; width: 126px; background: var(--rule-red); }
  .rule--green { left: 348px; width: 107px; background: var(--rule-green); }

  .flavour { position: absolute; left: 24px; line-height: 0.8; white-space: nowrap; }
  .flavour--red { top: 166px; font-size: 124px; color: var(--chili-red); letter-spacing: 4px; }
  .flavour--green { top: 160px; font-size: 76px; color: var(--leaf-green); letter-spacing: 4px; }
  .product { position: absolute; left: 22px; line-height: 0.8; color: var(--ink); font-size: 132px; letter-spacing: 6px; }
  .label--red .product { top: 264px; }
  .label--green .product { top: 223px; font-size: 124px; }
  .addition {
    position: absolute; left: 24px; top: 326px;
    display: flex; align-items: center;
    font-size: 54px; line-height: 0.8; color: var(--leaf-green); letter-spacing: 2px;
  }
  .addition__amp { font-size: 20px; margin-right: 8px; }

  .flame { position: absolute; border-radius: 50% 50% 46% 46% / 60% 60% 40% 40%; }
  .label--red .flame { left: 220px; top: 160px; width: 54px; height: 88px; background: linear-gradient(160deg, #e0474a, var(--chili-red-dark)); }
  .label--green .flame { left: 234px; top: 162px; width: 32px; height: 50px; background: linear-gradient(160deg, #8fcb52, var(--leaf-green-dark)); }

  .artwork { position: absolute; border-radius: 22px; }
  .label--red .artwork {
    left: 302px; top: 204px; width: 216px; height: 156px;
    background: linear-gradient(135deg, #d8403e 0%, #b7292a 60%, #9e1c1d 100%);
  }
  .label--green .artwork {
    left: 272px; top: 168px; width: 246px; height: 192px;
    background: linear-gradient(135deg, #8ccb52 0%, #6aab34 60%, #4f8e2b 100%);
  }

  .band { position: absolute; left: 0; right: 0; top: 396px; height: 41px; }
  .label--red .band { background: linear-gradient(90deg, var(--chili-red), #d43d40 60%, var(--chili-red-dark)); }
  .label--green .band { background: linear-gradient(90deg, #8fc54d, var(--leaf-green) 60%, var(--leaf-green-dark)); }
  .net-weight {
    position: absolute; left: 230px; top: 384px; width: 169px; height: 58px;
    background: var(--tag-black); border-radius: 4px;
    display: flex; align-items: center; justify-content: center;
    color: var(--tag-text); font-size: 19px; letter-spacing: 0.5px;
  }
</style>
</head>
<body>
<main class="canvas">
  <section class="label label--red">
    <div class="brand"><span class="brand__dot"></span><span class="brand__name">Zintara Chutney</span></div>
    <span class="rule rule--red"></span><span class="rule rule--green"></span>
    <h1 class="flavour flavour--red">Red</h1>
    <div class="flame" role="img" aria-label="Flame icon with chili silhouette"></div>
    <h2 class="product">Chili</h2>
    <div class="artwork" role="img" aria-label="Hand-drawn illustration of two red chili peppers"></div>
    <div class="band"></div>
    <div class="net-weight">NET WT. 8oz [227g]</div>
  </section>

  <section class="label label--green">
    <div class="brand"><span class="brand__dot"></span><span class="brand__name">Zintara Chutney</span></div>
    <span class="rule rule--red"></span><span class="rule rule--green"></span>
    <h1 class="flavour flavour--green">Green</h1>
    <div class="flame" role="img" aria-label="Small green flame icon"></div>
    <h2 class="product">Chili</h2>
    <p class="addition"><span class="addition__amp">&amp;</span>Coriander</p>
    <div class="artwork" role="img" aria-label="Hand-drawn illustration of green chili peppers with coriander sprigs"></div>
    <div class="band"></div>
    <div class="net-weight">NET WT. 8oz [227g]</div>
  </section>
</main>
</body>
</html>
```